Business Card Design Project

See the detainl of the Vortel company project I also have live: http://tasks.quillmarsh.com/task.aspx?id=382917

Reason: I am waiting to select a logo design and ideally the business card design will be from the same person

Industry/Entity Type

Business

```html
<!DOCTYPE html>
<html lang="en">
<head>
<meta charset="utf-8">
<title>Sorvane LLP – Business Card</title>
<link rel="stylesheet" href="https://fonts.googleapis.com/css2?family=Questrial&family=Open+Sans:wght@400;600;700&display=swap">
<style>
  :root {
    --brand-blue: #2289e6;
    --brand-blue-dark: #1a78d2;
    --row-blue: #c6e0fa;
    --card-white: #ffffff;
    --ink: #1c1c1c;
    --stage: #e9ebee;
  }
  * { box-sizing: border-box; margin: 0; padding: 0; }
  html, body {
    width: 1200px; height: 494px; overflow: hidden;
    background: var(--stage);
  }
  .card {
    position: absolute;
    left: 462px; top: 16px;
    width: 276px; height: 462px;
    background: var(--card-white);
    box-shadow: 0 2px 10px rgba(0,0,0,.12);
    font-family: "Open Sans", sans-serif;
    color: var(--ink);
  }
  .band { position: absolute; left: 0; right: 0; background: var(--brand-blue); }
  .band--top { top: 0; height: 9px; }
  .band--bottom { bottom: 0; height: 12px; }
  .band--bottom-thin { bottom: 20px; height: 3px; }

  .name-pill {
    position: absolute; top: 24px; left: 0;
    width: 160px; height: 19px;
    background: var(--brand-blue);
    border-radius: 0 7px 7px 0;
    color: #fff;
    font-family: "Questrial", sans-serif; font-weight: 700;
    font-size: 12px; letter-spacing: .5px;
    line-height: 19px; padding-left: 40px;
    text-transform: uppercase;
  }
  .job-title {
    position: absolute; top: 44px; left: 38px;
    color: var(--brand-blue);
    font-family: "Questrial", sans-serif; font-weight: 700;
    font-size: 11px;
  }
  .company-name {
    position: absolute; top: 64px; left: 24px;
    color: var(--brand-blue);
    font-family: "Questrial", sans-serif;
    font-size: 31px; letter-spacing: 1px;
  }
  .registered-office {
    position: absolute; top: 110px; right: 14px;
    text-align: right;
    color: var(--brand-blue-dark);
    font-family: "Questrial", sans-serif; font-weight: 700;
    font-size: 9.5px; line-height: 12px;
  }
  .web-pill {
    position: absolute; top: 150px; right: 0;
    width: 184px; height: 22px;
    background: var(--brand-blue);
    border-radius: 9px 0 0 9px;
    color: #fff;
    font-family: "Questrial", sans-serif; font-weight: 700;
    font-size: 13px; line-height: 22px; text-align: center;
  }
  .contact-list { position: absolute; top: 186px; left: 0; right: 0; list-style: none; }
  .contact-row {
    position: relative;
    margin-bottom: 6px;
    width: 256px;
    background: var(--row-blue);
    display: flex; align-items: center;
    padding-left: 72px;
    font-size: 11px; line-height: 13px;
  }
  .contact-row--double { height: 40px; }
  .contact-row--single { height: 32px; }
  .contact-icon {
    position: absolute; left: 24px; top: 50%;
    width: 18px; height: 18px; transform: translateY(-50%);
    fill: var(--brand-blue);
  }
</style>
</head>
<body>
  <article class="card">
    <div class="band band--top"></div>

    <div class="name-pill">Marcus Hale</div>
    <div class="job-title">Centre Director</div>
    <div class="company-name">SORVANE LLP</div>

    <address class="registered-office" style="font-style:normal">
      Registered Office:<br>
      Alder Court, 7B Harlow Rd,<br>
      Kestford KF2 6LP
    </address>

    <div class="web-pill">www.sorvane.co.uk</div>

    <ul class="contact-list">
      <li class="contact-row contact-row--double">
        <svg class="contact-icon" viewBox="0 0 18 18" aria-hidden="true">
          <rect x="5" y="1" width="8" height="16" rx="1.5" fill="none" stroke="var(--brand-blue)" stroke-width="1.4"/>
          <circle cx="9" cy="14.5" r=".9"/>
        </svg>
        <span>+44 (0)1632 518204<br>+44 (0)7700 259XXX</span>
      </li>
      <li class="contact-row contact-row--single">
        <svg class="contact-icon" viewBox="0 0 18 18" aria-hidden="true">
          <rect x="2" y="6" width="14" height="10" rx="1.5"/>
          <rect x="5" y="2" width="8" height="5" fill="none" stroke="var(--brand-blue)" stroke-width="1.2"/>
          <rect x="5" y="9" width="2" height="1.5" fill="#fff"/>
          <rect x="8" y="9" width="2" height="1.5" fill="#fff"/>
          <rect x="11" y="9" width="2" height="1.5" fill="#fff"/>
          <rect x="5" y="12" width="2" height="1.5" fill="#fff"/>
          <rect x="8" y="12" width="2" height="1.5" fill="#fff"/>
          <rect x="11" y="12" width="2" height="1.5" fill="#fff"/>
        </svg>
        <span>(0)1632 518205</span>
      </li>
      <li class="contact-row contact-row--single">
        <svg class="contact-icon" viewBox="0 0 18 18" aria-hidden="true">
          <rect x="1" y="4" width="16" height="11" rx="1"/>
          <path d="M1.5 4.5 L9 10.5 L16.5 4.5" fill="none" stroke="#fff" stroke-width="1.2"/>
        </svg>
        <span>ella.brook@sorvane.co.uk</span>
      </li>
      <li class="contact-row contact-row--double">
        <svg class="contact-icon" viewBox="0 0 18 18" aria-hidden="true">
          <path d="M9 1 C5.7 1 3.5 3.4 3.5 6.4 C3.5 10.5 9 17 9 17 C9 17 14.5 10.5 14.5 6.4 C14.5 3.4 12.3 1 9 1 Z"/>
          <circle cx="9" cy="6.5" r="2.2" fill="#fff"/>
        </svg>
        <span>41 Kestford Innovation Park<br>Reed Lane Kestford KF4 9QS</span>
      </li>
    </ul>

    <div class="band band--bottom-thin"></div>
    <div class="band band--bottom"></div>
  </article>
</body>
</html>
```